"Voltrane" it is a new and upcoming electrical company that can do all electrical jobs, test and tag

I need a webpage made for an electrical company. It can be basic but needs to be professional. I want a home page, about us page, Services page eg: Residential, Industrial, commercial electrical, installing of split system air-conditioners, test and tag, ariels, data, security camera's.
Lastly a contact us page.

The letterhead needs to be "Voltrane" in a green I think. Also under that a little sub heading saying " all of your electrical needs in the one company".

I also have paid for a host "webnestly" so I needs to be compatible with that software so it can be uploaded.

Target Market(s)

I mainly want to try and target business's with my ability to do test and tag.

Industry/Entity Type

Electrical

Coding

Coded - Design and coding required

Requirements
Must have
• It would be good if somewhere on the home page you have a section where they could put their name, contact details, and a brief description of what they want done. then a quote should be sent to my email address "reception@voltrane.com.au''

```html
<!DOCTYPE html>
<html lang="en">
<head>
<meta charset="utf-8">
<title>Voltrane – Electrical Services</title>
<link rel="stylesheet" href="https://fonts.googleapis.com/css2?family=Open+Sans:wght@400;600;700&family=Oswald:wght@600&display=swap">
<style>
:root{
  --green:#06aa06;
  --green-bright:#22dd22;
  --text:#333;
  --muted:#666;
  --line:#dcdcdc;
  --page:#f4f4f4;
  --topbar:#f6f6f6;
  --footer:#777;
  --footer-dark:#5a5a5a;
  --icon-grey:#777;
}
*{box-sizing:border-box;margin:0;padding:0}
html,body{width:1024px;height:1200px;overflow:hidden}
body{font-family:"Open Sans",Arial,sans-serif;color:var(--text);background:var(--page);position:relative}
.abs{position:absolute}

/* top bar */
.topbar{left:0;top:0;width:1024px;height:44px;background:var(--topbar);border-bottom:1px solid var(--line)}
.topbar .phone{right:117px;top:13px;font-size:14px;color:#444;display:flex;align-items:center;gap:6px}
.social{display:flex;gap:4px}
.social span{width:19px;height:19px;border-radius:50%;background:var(--icon-grey);display:block}
.topbar .social{right:44px;top:13px}

/* header */
.header{left:0;top:44px;width:1024px;height:80px;background:#fff}
.brand{display:flex;align-items:center;gap:7px}
.brand .mark{width:40px;height:40px;border-radius:50%;border:3px solid #777;flex:none}
.brand .name{font-size:21px;font-weight:700;color:var(--green-bright);letter-spacing:.3px;white-space:nowrap}
.header .brand{left:45px;top:14px}
.nav{right:43px;top:43px;display:flex;gap:16px;font-size:14.5px;color:#444}
.nav a{display:flex;align-items:center;gap:5px;color:inherit;text-decoration:none}
.nav a.active{color:var(--green)}

/* dropdown */
.dropdown{left:809px;top:114px;width:183px;background:#fff;border:1px solid #ccc;border-radius:3px;box-shadow:0 2px 5px rgba(0,0,0,.15);z-index:5;font-size:12.5px;color:#666;list-style:none;padding:1px 0}
.dropdown li{padding:6px 14px 6px;border-bottom:1px solid #e4e4e4;line-height:14px}
.dropdown li:last-child{border-bottom:0}
.dropdown li.active{background:var(--green);color:#fff}

/* hero */
.hero{left:0;top:124px;width:1024px;height:368px;background:linear-gradient(90deg,#ecebe6 0%,#e6e2da 24%,#b9a89a 45%,#8f8a6e 62%,#6f8a4d 80%,#83a35a 100%)}
.hero .fade{left:0;top:0;width:560px;height:368px;background:linear-gradient(90deg,rgba(240,238,234,1) 40%,rgba(240,238,234,0))}
.hero h1{left:44px;top:136px;font-family:"Oswald",Impact,sans-serif;font-size:33px;line-height:44px;font-weight:600;color:#2a2a2a;letter-spacing:-.5px}
.hero p{left:44px;top:187px;width:380px;font-size:13px;line-height:19px;color:#222}
.btn{background:var(--green);color:#fff;border-radius:3px;font-size:13px;display:flex;align-items:center;justify-content:center}
.hero .btn{left:45px;top:238px;width:104px;height:30px}
.dots{left:489px;top:336px;display:flex;gap:3px}
.dots span{width:13px;height:13px;border-radius:50%;border:2px solid #fff}
.dots span.on{background:var(--green)}

/* welcome */
.section-title{font-size:21px;font-weight:400;color:#222;line-height:28px}
.welcome-title{left:45px;top:519px}
.welcome-text{left:44px;top:550px;width:620px;font-size:13px;line-height:19.5px}
.features{left:57px;top:620px;list-style:none;font-size:13px;line-height:24px}
.features li{display:flex;align-items:center;gap:9px}
.services-title{left:45px;top:738px}
.services-photo{left:45px;top:776px;width:294px;height:208px;border-radius:3px;background:linear-gradient(135deg,#6d7a68,#9aa093 40%,#c8c3bc 60%,#4d4b55)}
.services-text{left:352px;top:779px;width:310px;font-size:13px;line-height:19px}
.services-text p+p{margin-top:19px}
.services-text a{color:var(--green);text-decoration:none;display:block;margin-top:6px}

/* quote */
.quote{left:684px;top:520px;width:296px;height:466px;background:#fff;border-radius:10px;box-shadow:0 0 6px rgba(0,0,0,.12);overflow:hidden}
.quote-head{height:72px;background:var(--green);color:#fff;text-align:center;padding-top:14px}
.quote-head h2{font-size:23px;font-weight:400;line-height:28px}
.quote-head h2 b{font-weight:700}
.quote-head p{font-size:12.5px}
.field{position:absolute;left:24px;font-size:13px;color:#333}
.input{position:absolute;left:80px;width:192px;border:1px solid #ccc;border-radius:3px;background:#fff}
.quote .btn{position:absolute;left:187px;top:414px;width:85px;height:30px;font-weight:600;font-size:13.5px}

/* footer */
.footer{left:0;top:1018px;width:1024px;height:134px;background:var(--footer);color:#fff}
.footer .brand{left:45px;top:47px}
.footer .brand .mark{border-color:#aaa}
.footer .brand .name{color:#aaa}
.contact{left:198px;top:24px;font-size:13px;line-height:21px;list-style:none}
.contact li{display:flex;align-items:flex-start;margin-bottom:5px}
.contact .ico{width:24px;height:21px;display:flex;align-items:center;flex:none}
.find{right:44px;top:46px;display:flex;align-items:center;gap:10px;font-size:13.5px}
.find .social span{width:23px;height:23px;background:#fff}
.footer-nav{right:43px;top:86px;font-size:14px}
.footer-nav span{margin:0 7px}
.copyright{left:0;top:1152px;width:1024px;height:48px;background:var(--footer-dark);color:#ddd;font-size:11.5px;text-align:center;line-height:48px}
</style>
</head>
<body>

<div class="abs topbar">
  <div class="abs phone">
    <svg width="10" height="16" viewBox="0 0 10 16"><rect x="1" y="1" width="8" height="14" rx="1.5" fill="none" stroke="#555" stroke-width="1.6"/><rect x="4" y="12" width="2" height="1.4" fill="#555"/></svg>
    +1 123&nbsp; 456 7890
  </div>
  <div class="abs social"><span></span><span></span><span></span></div>
</div>

<header class="abs header">
  <div class="abs brand"><span class="mark"></span><span class="name">Voltrane</span></div>
  <nav class="abs nav">
    <a href="#"><svg width="16" height="15" viewBox="0 0 16 15"><path d="M8 1 1 7.5h2V14h4V10h2v4h4V7.5h2z" fill="var(--green)"/></svg>Home</a>
    <a href="#"><svg width="16" height="16" viewBox="0 0 16 16"><circle cx="8" cy="5" r="4" fill="#999"/><path d="M1 16c0-5 3-7 7-7s7 2 7 7z" fill="#999"/></svg>About Us</a>
    <a href="#" class="active"><svg width="15" height="15" viewBox="0 0 16 16"><circle cx="8" cy="8" r="5" fill="none" stroke="var(--green)" stroke-width="3"/><g stroke="var(--green)" stroke-width="3"><path d="M8 0v3M8 13v3M0 8h3M13 8h3M2.3 2.3l2 2M11.7 11.7l2 2M2.3 13.7l2-2M11.7 4.3l2-2"/></g></svg>Services</a>
    <a href="#"><svg width="14" height="14" viewBox="0 0 16 16"><path d="M4 1 1.5 3.5C1 8 8 15 12.5 14.5L15 12l-3-3-2 2C8 10 6 8 5 6l2-2z" fill="#999"/></svg>Contact Us</a>
  </nav>
</header>

<ul class="abs dropdown">
  <li>Residential</li>
  <li class="active">Industrial</li>
  <li>Commercial electrical</li>
  <li>Installing of split system air-conditioners</li>
  <li>Test and tag</li>
  <li>Ariels</li>
  <li>Data</li>
  <li>Security camera's</li>
</ul>

<section class="abs hero" role="img" aria-label="Photo of a family sitting on the lawn in front of their brick home">
  <div class="abs fade"></div>
  <h1 class="abs">LOREM IPSUM DOLOR SIT</h1>
  <p class="abs">Lorem ipsum dolor sit amet, consectetur adipiscing elit. Ut sit amet metus ut lorem pharetra venenatis fermentum at nibh.</p>
  <div class="abs btn">READ MORE</div>
  <div class="abs dots"><span class="on"></span><span></span><span></span></div>
</section>

<h2 class="abs section-title welcome-title">WELCOME</h2>
<p class="abs welcome-text">Lorem ipsum dolor sit amet, consectetur adipiscing elit. Ut sit amet metus ut lorem pharetra venenatis fermentum at nibh. Nulla aliquet diam eu turpis convallis sit amet malesuada mi ultrices. In in velit massa, vitae condimentum leo.</p>
<ul class="abs features">
  <li><svg width="10" height="13" viewBox="0 0 10 13"><path d="M5 1a4 4 0 0 0-2.3 7.3V10h4.6V8.3A4 4 0 0 0 5 1z" fill="none" stroke="var(--green)" stroke-width="1.5"/><path d="M3 11.5h4" stroke="var(--green)" stroke-width="1.5"/></svg>Maecenas ultrices eros eget justo ultricies in mollis augue commodo.</li>
  <li><svg width="10" height="13" viewBox="0 0 10 13"><path d="M5 1a4 4 0 0 0-2.3 7.3V10h4.6V8.3A4 4 0 0 0 5 1z" fill="none" stroke="var(--green)" stroke-width="1.5"/><path d="M3 11.5h4" stroke="var(--green)" stroke-width="1.5"/></svg>Nullam sem tortor, volutpat non eleifend ut adipiscing in augue.</li>
  <li><svg width="10" height="13" viewBox="0 0 10 13"><path d="M5 1a4 4 0 0 0-2.3 7.3V10h4.6V8.3A4 4 0 0 0 5 1z" fill="none" stroke="var(--green)" stroke-width="1.5"/><path d="M3 11.5h4" stroke="var(--green)" stroke-width="1.5"/></svg>Aliquam at eros magna tiam tempus est quis massa .</li>
  <li><svg width="10" height="13" viewBox="0 0 10 13"><path d="M5 1a4 4 0 0 0-2.3 7.3V10h4.6V8.3A4 4 0 0 0 5 1z" fill="none" stroke="var(--green)" stroke-width="1.5"/><path d="M3 11.5h4" stroke="var(--green)" stroke-width="1.5"/></svg>Sagittis sit amet lobortis quam malesuada.</li>
</ul>

<h2 class="abs section-title services-title">OUR SERVICES</h2>
<div class="abs services-photo" role="img" aria-label="Photo of a tradesman working at a drill press in a workshop"></div>
<div class="abs services-text">
  <p>Lorem ipsum dolor sit amet, consectetur adipiscing elit. Ut sit amet metus ut lorem pharetra venenatis fermentum at nibh.</p>
  <p>Nulla aliquet diam eu turpis convallis sit amet mal esu ada mi ultrices. In in velit massa vitae co ndim entum leo. In interdum blandit ornare. Vivamus malesuada arcu in tellus consectetur rhoncus.</p>
  <a href="#">Read More</a>
</div>

<form class="abs quote">
  <div class="quote-head">
    <h2>REQUEST A <b>QUOTE</b></h2>
    <p>Lorem ipsum dolor sit amet consectetur</p>
  </div>
  <label class="field" style="top:96px">Name:</label><div class="input" style="top:90px;height:28px"></div>
  <label class="field" style="top:137px">Email:</label><div class="input" style="top:131px;height:28px"></div>
  <label class="field" style="top:178px">Phone:</label><div class="input" style="top:172px;height:28px"></div>
  <label class="field" style="top:214px">Address:</label><div class="input" style="top:212px;height:54px"></div>
  <label class="field" style="top:275px">Messages:</label>
  <div class="input" style="left:24px;width:248px;top:300px;height:100px"></div>
  <div class="btn">SUBMIT</div>
</form>

<footer class="abs footer">
  <div class="abs brand"><span class="mark"></span><span class="name">Voltrane</span></div>
  <ul class="abs contact">
    <li><span class="ico"><svg width="10" height="14" viewBox="0 0 10 14"><rect x="1" y="1" width="8" height="12" rx="1.5" fill="none" stroke="#ddd" stroke-width="1.5"/></svg></span>+1 123&nbsp; 456 7890</li>
    <li><span class="ico"><svg width="13" height="10" viewBox="0 0 13 10"><rect width="13" height="10" fill="#ddd"/><path d="M0 0l6.5 5L13 0" fill="none" stroke="#777" stroke-width="1.2"/></svg></span>reception@voltrane.com.au</li>
    <li><span class="ico"><svg width="10" height="13" viewBox="0 0 10 13"><path d="M5 0a4.5 4.5 0 0 0-4.5 4.5C.5 8 5 13 5 13s4.5-5 4.5-8.5A4.5 4.5 0 0 0 5 0z" fill="#ddd"/><circle cx="5" cy="4.5" r="1.6" fill="#777"/></svg></span><span>XXX Some Street Address, City<br>State Australia</span></li>
  </ul>
  <div class="abs find">Find us on <div class="social"><span></span><span></span><span></span></div></div>
  <div class="abs footer-nav">Home<span>|</span>About Us<span>|</span>Services<span>|</span>Contact Us</div>
</footer>
<div class="abs copyright">Copyright © 2014 Voltrane. All Rights Reserved.</div>

</body>
</html>
```